Electrical Contractor Company Profile

We need a Brochure that is more entertaining than our current Company Profile Document. We have lots of great experience and awesome looking jobs in our portfolio but need a document that we can either print of send in electronic format to accompany some of our submissions.

We are ideally looking for something 9-10 pages in A4 with some of the pages opening out to A3.

We are looking for a document that is professional and smart however shows the colour and quality that we feel we offer to prospective clientele.

I have included the current Company Profile and Logo along with a number of images of completed projects that may be of use.

Target Market(s)

Builders, Facility Managers, Engineers, Decision makers

Industry/Entity Type

Electrical

Font styles to use
Sans Serif

Colors

Designer to choose colors to be used in the design.

Requirements
Must have
• - Modern look with a focus on sustainability
• - Clean Simple and Professional
• - Incorporate our Logo
• Core Business Lines need to be across an A3 opening page and have photos relating to these lines Solar, Communications and any of the projects.
Nice to have
• Lots of colour and photos mixed with the text
Should not have
• Lightning bolts or corny symbols

```html
<!DOCTYPE html>
<html lang="en">
<head>
<meta charset="utf-8">
<title>Voltara Electrical — Company Profile Spreads</title>
<link rel="stylesheet" href="https://fonts.googleapis.com/css2?family=Arimo:wght@400;700&family=Open+Sans:ital,wght@0,400;0,700;1,400;1,700&family=Roboto+Condensed:ital,wght@0,700;1,800&display=swap">
<style>
:root{
  --stage:#231f20;
  --navy:#1d4f8f;
  --navy-deep:#173f75;
  --orange:#f6921e;
  --orange-soft:#f9ab4f;
  --white:#ffffff;
  --label-white:#f2f2f2;
  --label-orange:#f7a54a;
  --label-blue:#9ec3e6;
  --label-grey:#c9c9c9;
}
*{margin:0;padding:0;box-sizing:border-box}
html,body{width:1008px;height:1200px;overflow:hidden;background:var(--stage)}
body{position:relative;font-family:"Open Sans",Arial,sans-serif;color:var(--white)}
.spread{position:absolute;width:432px;height:304px;overflow:hidden;background:var(--navy)}
.spread::after{content:"";position:absolute;left:215px;top:0;width:2px;height:100%;background:linear-gradient(90deg,rgba(0,0,0,.25),rgba(255,255,255,.08))}
.s1{left:62px;top:64px;background:var(--orange)}
.s2{left:516px;top:62px}
.s3{left:62px;top:430px}
.s4{left:516px;top:430px}
.s5{left:62px;top:800px}
.s6{left:516px;top:802px}
.label{position:absolute;font-family:"Arimo",Arial,sans-serif;font-size:21px;line-height:1}
.label.white{color:var(--label-white)}
.label.orange{color:var(--label-orange)}
.label.blue{color:var(--label-blue)}
.label.grey{color:var(--label-grey)}
.abs{position:absolute}
.photo{position:absolute}
.brand{position:absolute;display:flex;align-items:center;gap:3px;font-family:"Open Sans",Arial,sans-serif;font-weight:700;font-size:10px;letter-spacing:.2px;color:var(--white);white-space:nowrap}
.brand .dot{width:9px;height:9px;border-radius:50%;background:var(--white)}
.brand.on-light{color:var(--navy)}
.brand.on-light .dot{background:var(--orange)}
.header-rule{position:absolute;height:1px;background:rgba(255,255,255,.55)}
.tiny{font-size:3.6px;line-height:1.45;color:var(--white)}
.tiny b{color:var(--orange)}
.tiny.on-orange b{color:var(--navy)}
.tiny ul{list-style:none}
.tiny li::before{content:"■ ";font-size:2.6px}
.vertical-head{position:absolute;font-family:"Roboto Condensed",Arial,sans-serif;font-weight:800;font-style:italic;color:var(--white);writing-mode:vertical-rl;transform:rotate(180deg);white-space:nowrap;line-height:1}
.orange-band{position:absolute;background:var(--orange)}
.quote{font-style:italic;font-size:3.6px;line-height:1.4;color:var(--orange)}
.lead{font-style:italic;font-size:4px;line-height:1.4;color:var(--orange)}
table.projects{position:absolute;border-collapse:collapse;font-size:2.7px;line-height:1.15;background:var(--orange);color:#fff}
table.projects th{background:var(--navy-deep);font-weight:700;padding:2px 1px;text-align:center}
table.projects td{padding:2.3px 1.5px;border-bottom:.5px solid rgba(255,255,255,.55);border-right:.5px solid rgba(255,255,255,.35)}
.side-title{position:absolute;font-family:"Roboto Condensed",Arial,sans-serif;font-weight:800;font-style:italic;font-size:12px;color:rgba(255,255,255,.25);writing-mode:vertical-rl;transform:rotate(180deg);white-space:nowrap}
.big-head{position:absolute;font-family:"Roboto Condensed",Arial,sans-serif;font-weight:700;font-size:13px;line-height:.82;color:var(--white)}
</style>
</head>
<body>

<section class="spread s1">
  <div class="abs" style="left:74px;top:0;width:140px;height:80px;background:var(--white)"></div>
  <div class="abs" style="left:217px;top:0;width:138px;height:80px;background:var(--white)"></div>
  <div class="brand on-light" style="left:96px;top:28px;font-size:12px"><span class="dot"></span>VOLTARA</div>
  <div class="brand on-light" style="left:238px;top:28px;font-size:12px"><span class="dot"></span>VOLTARA</div>
  <div class="photo" role="img" aria-label="Service van parked outside a colourful building" style="left:74px;top:56px;width:141px;height:130px;background:linear-gradient(160deg,#e4a23a 0%,#8fa3b4 40%,#e8ecef 62%,#6f7a82 100%)"></div>
  <div class="photo" role="img" aria-label="Retail arcade walkway with mural artwork" style="left:217px;top:56px;width:138px;height:130px;background:linear-gradient(135deg,#d6c9a2 0%,#7a5e3f 45%,#c7b9a4 70%,#5b4a3a 100%)"></div>
  <svg class="abs" style="left:0;top:0" width="432" height="304" viewBox="0 0 432 304" aria-hidden="true">
    <path d="M0 200 Q110 170 215 188 Q300 170 360 182 L360 304 L0 304 Z" fill="#1d4f8f"/>
  </svg>
  <div class="vertical-head" style="left:368px;top:14px;font-size:22px;font-family:'Roboto Condensed',Arial,sans-serif;font-weight:700;font-style:normal;line-height:.9;transform:rotate(180deg)">COMPANY<br>PROFILE</div>
  <div class="brand" style="left:10px;top:215px;font-size:8px"><span class="dot" style="width:7px;height:7px"></span>VOLTARA</div>
  <div class="tiny abs" style="left:10px;top:238px;width:70px">Licence No. EC 004821<br>Tel. 1300 555 014<br>hello@voltara.example<br>www.voltara.example<br><br>ABN 00 111 222 333<br>12 Harbour Street<br>East Rivergate WA 6104<br>PO Box 410<br>Rivergate WA 6932</div>
  <div class="tiny abs" style="left:368px;top:238px;width:62px">Licence No. EC 004821<br>Tel. 1300 555 014<br>hello@voltara.example<br>www.voltara.example<br><br>ABN 00 111 222 333<br>12 Harbour Street<br>East Rivergate WA 6104<br>PO Box 410<br>Rivergate WA 6932</div>
</section>
<div class="label white" style="left:77px;top:376px">Back Cover Page 12</div>
<div class="label white" style="left:343px;top:376px">Front Cover</div>

<section class="spread s2">
  <div class="brand" style="left:134px;top:8px"><span class="dot"></span>VOLTARA</div>
  <div class="brand" style="left:350px;top:8px"><span class="dot"></span>VOLTARA</div>
  <div class="header-rule" style="left:134px;top:25px;width:78px"></div>
  <div class="header-rule" style="left:350px;top:25px;width:78px"></div>
  <div class="photo" role="img" aria-label="Tree-lined path through a park under blue sky" style="left:0;top:30px;width:134px;height:274px;background:linear-gradient(180deg,#2f6fb8 0%,#8dbde6 35%,#5c7f3a 52%,#9a5a5a 70%,#7a4545 100%)"></div>
  <div class="orange-band" style="left:134px;top:40px;width:214px;height:264px"></div>
  <div class="tiny abs" style="left:140px;top:155px;width:70px">Founded in 2006, Voltara is an award winning firm offering broad electrical skills across commercial, industrial and community sectors.<br><br>Voltara has the capacity and capability to complete contracts for large and small clients with a focus on private and government agencies.</div>
  <div class="abs" style="left:140px;top:228px;font-size:4.5px;font-style:italic;font-weight:700;color:var(--navy)">Our services include:</div>
  <div class="tiny on-orange abs" style="left:140px;top:236px;width:70px"><ul><li>Electrical projects</li><li>Planned and reactive maintenance</li><li>Design and construct</li><li>Electrical drafting</li><li>Communications</li><li>Minor works</li><li>Solar power generation and storage</li><li>Electronic lighting control</li></ul></div>
  <div class="tiny abs" style="left:290px;top:196px;width:54px">Our ability to deliver successful projects was recognised at both the state and national excellence awards for lighting and best commercial project.<br><br>With an office and warehouse placed centrally, Voltara is well placed to service the broader metropolitan area and regional areas of the state.</div>
  <div class="tiny abs" style="left:350px;top:40px;width:78px">Voltara enjoys a high volume of repeat business, which is a result of our:<ul style="margin-top:3px"><li>Commitment to consistently high quality results</li><li>Priority of dealing openly with clients and suppliers to build lasting positive relations</li><li>Innovation and ability to adopt new technology</li><li>Knowledgeable staff who can complete complex projects</li><li>Team ability to develop designs and work systems to meet site needs</li><li>Proven approach to project management</li></ul></div>
  <div class="photo" role="img" aria-label="Shopping arcade interior with shopfront signage" style="left:348px;top:120px;width:84px;height:184px;background:linear-gradient(170deg,#8a7a66 0%,#3a3028 40%,#c8ad88 70%,#6b5a48 100%)"></div>
</section>
<div class="label orange" style="left:589px;top:373px">Page 2</div>
<div class="label grey" style="left:775px;top:373px">Page 3</div>

<section class="spread s3">
  <div class="brand" style="left:130px;top:10px"><span class="dot"></span>VOLTARA</div>
  <div class="brand" style="left:348px;top:10px"><span class="dot"></span>VOLTARA</div>
  <div class="header-rule" style="left:130px;top:27px;width:80px"></div>
  <div class="header-rule" style="left:348px;top:27px;width:80px"></div>
  <div class="orange-band" style="left:140px;top:30px;width:75px;height:274px"></div>
  <div class="orange-band" style="left:217px;top:30px;width:56px;height:274px"></div>
  <div class="vertical-head" style="left:142px;top:36px;font-size:14px">CORE BUSINESS</div>
  <div class="vertical-head" style="left:219px;top:116px;font-size:14px">CORE BUSINESS</div>
  <div class="tiny abs" style="left:10px;top:42px;width:120px">Voltara maintains five core lines of business:<br><br><b>1 Breakdown and response</b> – providing a 24/7 call out service to a number of key clients. This team is high energy and responsive in most situations, with repeat business earned by keeping clients happy.<br><br><b>2 Planned Maintenance</b> – This team services over 500 sites across the metro area, carrying out planned testing and repair of all electrical infrastructure needed by our clients. This includes emergency lighting along with thermal imaging surveys.<br><br><b>3 Electrical Projects</b> – this line of business is tasked with completing contracts both large and small in value. Team members are skilled in installing various kinds of electrical systems with the high quality workmanship expected in this highly competitive sector.</div>
  <div class="photo" role="img" aria-label="Modern white institute building with curved facade" style="left:0;top:155px;width:215px;height:90px;background:linear-gradient(180deg,#a9c6e0 0%,#e9eef1 45%,#8c939a 75%,#4d5a3e 100%)"></div>
  <div class="quote abs" style="left:145px;top:250px;width:66px">"The finished product at the site is of excellent quality. We were extremely impressed with the level of service." Daniel Harlow, Brickfield Builders</div>
  <div class="tiny abs" style="left:278px;top:34px;width:148px"><b>4 Communications</b> – our staff are highly skilled and carry open cabling licences and fibre qualifications. The company owns test equipment and regularly invests in continued training of staff. We can supply both design and installation services for private networks, providing a certified solution to any copper and fibre optic needs.<br><br><b>5 Solar PV</b> – Focusing on the commercial market we are able to offer fully designed solutions for photovoltaic systems up to 200kW designed to suit a client's needs and budget. With highly trained consultants and installers we pride ourselves on offering good value for money and clarity on project benefits.<br><br><b>6 Technology Services</b> – With strong base knowledge and an ongoing commitment to training and innovation, we are able to offer solutions for energy management, energy conservation, electronic lighting control, power monitoring and performance auditing, providing our clients with useful reporting and a better understanding of their assets.</div>
  <div class="photo" role="img" aria-label="Switchboard cabinets and electrical panels in a plant room" style="left:273px;top:140px;width:159px;height:164px;background:linear-gradient(135deg,#d9692b 0%,#b7502a 35%,#c9c9c6 55%,#8d8f90 100%)"></div>
  <div class="quote abs" style="left:222px;top:250px;width:50px">"The finished product is of excellent quality. We have been very impressed with the ease of our working relationship." Mara Quint, Eastline Property</div>
</section>
<div class="label orange" style="left:133px;top:740px">Page 4</div>
<div class="label orange" style="left:319px;top:740px">Page 5</div>

<section class="spread s4">
  <div class="brand" style="left:134px;top:10px"><span class="dot"></span>VOLTARA</div>
  <div class="brand" style="left:350px;top:10px"><span class="dot"></span>VOLTARA</div>
  <div class="header-rule" style="left:0;top:27px;width:215px"></div>
  <div class="header-rule" style="left:217px;top:27px;width:215px"></div>
  <div class="big-head" style="left:12px;top:36px">PROVEN<br>MANAGEMENT<br>SYSTEMS</div>
  <div class="abs" style="left:12px;top:68px;width:90px;font-size:3.6px;font-weight:700;font-style:italic;line-height:1.35">Our commitment to quality, health and safety and the environment places Voltara apart from our many competitors.</div>
  <div class="orange-band" style="left:136px;top:48px;width:79px;height:256px"></div>
  <div class="orange-band" style="left:217px;top:48px;width:118px;height:256px"></div>
  <div class="vertical-head" style="left:137px;top:52px;font-size:13px">QUALITY</div>
  <div class="vertical-head" style="left:318px;top:54px;font-size:13px">ENVIRONMENT</div>
  <div class="photo" role="img" aria-label="Grid of coloured data cables in a communications rack" style="left:0;top:94px;width:136px;height:134px;background:linear-gradient(135deg,#d94f6a 0%,#3a7bd5 30%,#e9d24a 55%,#4fa36b 80%,#c95ad0 100%)"></div>
  <div class="quote abs" style="left:12px;top:238px;width:110px;color:var(--white)">"We found them to be professional, courteous and able to carry out their works both on time and on budget. We will be happy to use them on future projects." Daniel Harlow, Brickfield Builders</div>
  <div class="tiny abs" style="left:140px;top:110px;width:70px">Voltara is committed to providing clients with services, products and solutions in a reliable and consistent manner. With our certified management system aligned to ISO 9001 we ensure a consistent result is achieved in all cases.<br><br>Our quality system ensures:<ul><li>Consistent communication with all stakeholders</li><li>Experienced and qualified staff are deployed</li><li>Flexible workforce ready to work across all types of business</li><li>Clearly defined roles and responsibilities for all staff</li><li>Correct training and support for all staff</li><li>Quality monitoring and reporting throughout the entire work process</li></ul></div>
  <div class="tiny abs" style="left:222px;top:118px;width:78px">Voltara strives to deliver all projects in an environmentally responsible manner. We have a comprehensive set of policies and procedures that ensure we comply with all relevant environmental legislation, codes of practice and contract conditions. We also conduct business with suppliers and subcontractors who have a commitment to responsible environmental management.</div>
  <div class="photo" role="img" aria-label="Covered outdoor pavilion lit at dusk" style="left:222px;top:168px;width:112px;height:76px;background:linear-gradient(180deg,#2c3e66 0%,#6e7fa6 40%,#c79b5a 70%,#5a4630 100%)"></div>
  <div class="tiny abs" style="left:222px;top:252px;width:80px;font-style:italic">"We have a long history on various projects and have been extremely satisfied with the level of quality and customer service we have received." Owen Pratt, Keystone Construction</div>
  <div class="photo" role="img" aria-label="Rows of solar panels on a commercial roof" style="left:335px;top:48px;width:97px;height:70px;background:linear-gradient(180deg,#bcd7ef 0%,#e6eef5 35%,#3e5c86 60%,#22395e 100%)"></div>
  <div class="abs" style="left:340px;top:124px;font-family:'Roboto Condensed',Arial,sans-serif;font-weight:800;font-style:italic;font-size:7px;line-height:.95">WORKPLACE<br>HEALTH AND SAFETY</div>
  <div class="abs" style="left:340px;top:140px;font-size:4px;font-style:italic">Our high level of safety is achieved by:</div>
  <div class="tiny abs" style="left:340px;top:148px;width:88px"><ul><li>Planning, developing, implementing and monitoring full health, safety and welfare programs</li><li>Promoting understanding of health, safety and welfare as a normal part of all aspects of work</li><li>Developing site specific systems and plans to meet each project</li><li>Ensuring staff receive suitable safety and first aid training</li><li>Providing a healthy and safe workplace</li></ul><br>Voltara uses a full HSEQ Management System tailored to suit our business. The system is:<ul><li>Certified to the WHS Code 2014</li><li>Fully meets requirements of AS/NZS 4801 OHS Management Systems</li></ul></div>
  <div class="abs" style="left:340px;top:258px;width:88px;font-size:4.5px;font-weight:700;font-style:italic;line-height:1.3">Our system is<br>audited twice annually<br>to ensure<br>that the system is being utilized</div>
</section>
<div class="label blue" style="left:609px;top:740px">Page 6</div>
<div class="label blue" style="left:797px;top:740px">Page 7</div>

<section class="spread s5">
  <div class="brand" style="left:130px;top:10px"><span class="dot"></span>VOLTARA</div>
  <div class="brand" style="left:348px;top:10px"><span class="dot"></span>VOLTARA</div>
  <div class="header-rule" style="left:0;top:27px;width:215px"></div>
  <div class="header-rule" style="left:217px;top:27px;width:215px"></div>
  <div class="lead abs" style="left:35px;top:42px;width:175px">Voltara has been pleased to complete the following projects:</div>
  <div class="side-title" style="left:20px;top:60px">DELIVERED PROJECTS</div>
  <table class="projects" style="left:35px;top:58px;width:175px">
    <tr><th>PROJECT</th><th>CATEGORY</th><th>DESCRIPTION</th><th>YEAR</th><th>VALUE</th></tr>
    <tr><td>Harbour Hotel</td><td>Hotel</td><td>New 4 storey apartment hotel</td><td>2016</td><td>1.6M</td></tr>
    <tr><td>Westgate School</td><td>Education</td><td>New teaching and admin area</td><td>2016</td><td>1.2M</td></tr>
    <tr><td>South Ridge College</td><td>Education</td><td>Site power upgrade</td><td>2016</td><td>1.0M</td></tr>
    <tr><td>St Anne's College</td><td>Education</td><td>New multiple teaching blocks</td><td>2016</td><td>1.8M</td></tr>
    <tr><td>Bay Street Housing</td><td>Residential</td><td>New 12 storey building</td><td>2016</td><td>1.9M</td></tr>
    <tr><td>Civic Corps Hall</td><td>Commercial</td><td>New headquarters</td><td>2015</td><td>800K</td></tr>
    <tr><td>Central Tower</td><td>Commercial</td><td>Supply upgrade to office tower</td><td>2015</td><td>1.4M</td></tr>
    <tr><td>Sports Institute</td><td>Commercial</td><td>Training centre and admin</td><td>2015</td><td>1.0M</td></tr>
    <tr><td>Lakeview Homes</td><td>Residential</td><td>New 28 boutique townhouses</td><td>2015</td><td>1.4M</td></tr>
    <tr><td>Northgate Mall</td><td>Retail</td><td>Distribution upgrade to shops</td><td>2015</td><td>450K</td></tr>
    <tr><td>Marlow Centre</td><td>Commercial</td><td>Function centre and tavern</td><td>2014</td><td>1.3M</td></tr>
    <tr><td>Hillside College</td><td>Education</td><td>Extension of teaching block</td><td>2014</td><td>650K</td></tr>
    <tr><td>Riverside College</td><td>Education</td><td>Multi-function sports hall</td><td>2014</td><td>1.1M</td></tr>
    <tr><td>West Park Primary</td><td>Education</td><td>New teaching block</td><td>2014</td><td>600K</td></tr>
  </table>
  <div class="photo" role="img" aria-label="Collage of completed project photos: bar interiors, ceiling lighting, curved facade, feature artwork, colourful wall, solar panels and cabling" style="left:217px;top:34px;width:215px;height:270px;background:linear-gradient(160deg,#3d6ea8 0%,#c58a3c 25%,#6a4a2e 45%,#d97a45 60%,#4f86b8 78%,#e0b84a 100%)"></div>
</section>
<div class="label white" style="left:137px;top:1116px">Page 8</div>
<div class="label white" style="left:323px;top:1116px">Page 9</div>

<section class="spread s6">
  <div class="brand" style="left:134px;top:10px"><span class="dot"></span>VOLTARA</div>
  <div class="brand" style="left:350px;top:10px"><span class="dot"></span>VOLTARA</div>
  <div class="header-rule" style="left:0;top:27px;width:215px"></div>
  <div class="header-rule" style="left:217px;top:27px;width:215px"></div>
  <div class="lead abs" style="left:36px;top:42px;width:175px">Voltara has been pleased to complete the following projects:</div>
  <div class="side-title" style="left:22px;top:58px">DELIVERED PROJECTS</div>
  <table class="projects" style="left:36px;top:58px;width:175px">
    <tr><th>PROJECT</th><th>CATEGORY</th><th>DESCRIPTION</th><th>YEAR</th><th>VALUE</th></tr>
    <tr><td>Greenfield College</td><td>Education</td><td>New teaching block</td><td>2014</td><td>750K</td></tr>
    <tr><td>Eastfield Square</td><td>Retail</td><td>Upgrade of retail areas</td><td>2014</td><td>1.0M</td></tr>
    <tr><td>Parkside Apartments</td><td>Residential</td><td>Multi storey 104 unit block</td><td>2014</td><td>2.5M</td></tr>
    <tr><td>Royal Health Clinic</td><td>Health</td><td>New consulting rooms</td><td>2013</td><td>1.2M</td></tr>
    <tr><td>City Youth Hostel</td><td>Commercial</td><td>Multi storey hostel building</td><td>2013</td><td>2.6M</td></tr>
    <tr><td>Art Gallery Wing</td><td>Commercial</td><td>Lighting upgrade to gallery</td><td>2013</td><td>600K</td></tr>
    <tr><td>Trade Training Centre</td><td>Education</td><td>Plumbing trade centre</td><td>2013</td><td>750K</td></tr>
    <tr><td>Quay Plaza</td><td>Retail</td><td>New shopping centre and car park</td><td>2013</td><td>1.4M</td></tr>
    <tr><td>Terrace Apartments</td><td>Residential</td><td>Boutique apartments</td><td>2013</td><td>450K</td></tr>
    <tr><td>Medical House</td><td>Health</td><td>New imaging facility</td><td>2013</td><td>850K</td></tr>
    <tr><td>Fort View Building</td><td>Residential</td><td>Multi storey 96 unit block</td><td>2012</td><td>1.5M</td></tr>
    <tr><td>Coastal Nursery</td><td>Commercial</td><td>Works and viewing upgrade</td><td>2012</td><td>1.1M</td></tr>
    <tr><td>Ridge School</td><td>Education</td><td>Power supply replacement</td><td>2012</td><td>1.1M</td></tr>
    <tr><td>Trade Association HQ</td><td>Commercial</td><td>Office and fit out</td><td>2012</td><td>2.4M</td></tr>
    <tr><td>Tech Institute North</td><td>Education</td><td>Teaching facility fit out</td><td>2012</td><td>800K</td></tr>
  </table>
  <div class="orange-band" style="left:222px;top:34px;width:82px;height:270px"></div>
  <div class="photo" role="img" aria-label="Warm lit brewery bar interior with pendant lights" style="left:304px;top:34px;width:128px;height:270px;background:linear-gradient(170deg,#f2e6c8 0%,#c99a52 35%,#6e4a24 65%,#d8b072 100%)"></div>
  <div class="quote abs" style="left:346px;top:44px;width:80px;color:var(--navy)">"The final quality of workmanship at the venue is a reflection of the care that Voltara put into this project." Owen Pratt, Keystone Construction</div>
  <div class="vertical-head" style="left:287px;top:110px;font-size:14px">SUMMARY</div>
  <div class="tiny abs" style="left:227px;top:184px;width:56px">Voltara is an award winning company that offers:<ul><li>Experience with a broad range of commercial projects</li><li>An innovative approach</li><li>Experienced and knowledgeable staff</li><li>Thorough project planning</li><li>Strong operational systems</li><li>Effective communication with everyone involved in the project</li><li>A commitment to quality workmanship</li></ul></div>
  <div class="abs" style="left:227px;top:264px;width:62px;font-size:5px;font-style:italic;line-height:1.3">We look forward to applying our skills and assisting you with your project.</div>
</section>
<div class="label white" style="left:595px;top:1114px">Page 10</div>
<div class="label white" style="left:781px;top:1114px">Page 11</div>

</body>
</html>
```